The Farrowdale Penick Firm

We are a real estate and business acquisition services company that provides consulting services to large companies and individuals. The company provided nationwide services to companies looking to expand through opening new locations or buying other companies in their field. We work very close with attorneys, accountants, banks/financial institutions and high level executives and business owners.

Target Market(s)

CEO, VP, business owners and bankers.

Industry/Entity Type

Real Estate

Requirements
Must have
• I am looking for a design that looks very professional and has a classic, trustworthy, professional feeling. I want the letterhead and return address to look formal and official so this it is not tossed out as junk mail. FP or FPF can be used in a logo style part but that is not required. Our tag line is "Real Estate and Business Acquisition Services". This should be on the letter head but not on the return address. It does not need a lot of color but I will leave that to your tasteful choice. It should be rich and formal looking.
Should not have
• I do not want anything that looks like a cartoon drawing or figure. Use font that gives a strong trustworthy look. We are not a law firm so no scales or gavels. A law firm sort of look or feel is OK.

```html
<!DOCTYPE html>
<html lang="en">
<head>
<meta charset="utf-8">
<title>The Farrowdale Penick Firm — Stationery</title>
<link rel="stylesheet" href="https://fonts.googleapis.com/css2?family=Mulish:wght@400;700&display=swap">
<style>
  :root {
    --backdrop: #d8d4cf;
    --paper: #ffffff;
    --paper-edge: #e4e4e4;
    --ink: #2b2b2b;
    --ink-soft: #5a5a5a;
    --rule: #8a8a8a;
    --shadow: rgba(0, 0, 0, 0.18);
  }
  * { box-sizing: border-box; margin: 0; padding: 0; }
  html, body {
    width: 1200px;
    height: 790px;
    overflow: hidden;
  }
  body {
    position: relative;
    background: var(--backdrop);
    font-family: "Mulish", "Helvetica Neue", Arial, sans-serif;
    color: var(--ink);
  }
  .sheet {
    position: absolute;
    background: var(--paper);
    border: 1px solid var(--paper-edge);
    box-shadow: 0 2px 8px var(--shadow);
  }
  .brand-mark {
    position: absolute;
    left: 50%;
    transform: translateX(-50%);
    background: var(--ink);
  }
  .firm-name {
    position: absolute;
    left: 0;
    right: 0;
    text-align: center;
    font-weight: 400;
    white-space: nowrap;
  }
  .tagline {
    position: absolute;
    left: 0;
    right: 0;
    text-align: center;
    font-size: 9.5px;
    letter-spacing: 0.14em;
    text-transform: uppercase;
    color: var(--ink-soft);
    white-space: nowrap;
  }
  .address-line {
    position: absolute;
    display: flex;
    align-items: center;
    gap: 10px;
    font-size: 12px;
    white-space: nowrap;
  }
  .address-line::before {
    content: "";
    display: block;
    width: 1px;
    height: 22px;
    background: var(--rule);
  }

  /* Letterhead */
  .letterhead { left: 40px; top: 33px; width: 552px; height: 713px; }
  .letterhead .brand-mark { top: 32px; width: 14px; height: 14px; }
  .letterhead .firm-name { top: 62px; font-size: 20px; }
  .letterhead .tagline { top: 94px; }
  .letterhead .address-line { left: 150px; bottom: 16px; }

  /* Envelope */
  .envelope { left: 612px; top: 402px; width: 550px; height: 343px; }
  .envelope .brand-mark { top: 30px; width: 14px; height: 14px; }
  .envelope .firm-name { top: 59px; font-size: 20px; }
  .envelope .address-line { left: 148px; bottom: 16px; }

  /* Business cards */
  .business-card { width: 230px; height: 128px; }
  .business-card .brand-mark { top: 13px; width: 7px; height: 7px; }
  .business-card .firm-name { top: 25px; font-size: 10px; }
  .card-contact {
    position: absolute;
    left: 46px;
    bottom: 16px;
    display: flex;
    align-items: stretch;
    gap: 6px;
  }
  .card-person { text-align: right; }
  .card-person .person-name { font-size: 9.5px; font-weight: 700; }
  .card-person .person-title { font-size: 7px; }
  .card-divider { width: 1px; background: var(--rule); }
  .card-address { font-size: 7px; line-height: 1.45; padding-top: 1px; }

  .card-stack-back { left: 421px; top: 193px; height: 155px; }
  .card-stack-middle { left: 421px; top: 216px; height: 132px; }
  .card-stack-front { left: 410px; top: 238px; height: 134px; }
  .card-single { left: 688px; top: 130px; }
</style>
</head>
<body>

  <section class="sheet letterhead" aria-label="Letterhead">
    <span class="brand-mark" aria-hidden="true"></span>
    <h1 class="firm-name">The Farrowdale Penick Firm</h1>
    <p class="tagline">Real Estate and Business Acquisition Services</p>
    <p class="address-line">4820 Larkmoor Pike, Suite 210 Nashville, TN&nbsp; 37211</p>
  </section>

  <div class="sheet business-card card-stack-back" aria-hidden="true">
    <span class="brand-mark"></span>
  </div>
  <div class="sheet business-card card-stack-middle" aria-hidden="true">
    <span class="brand-mark"></span>
  </div>

  <section class="sheet business-card card-stack-front" aria-label="Business card">
    <span class="brand-mark" aria-hidden="true"></span>
    <h2 class="firm-name">The Farrowdale Penick Firm</h2>
    <div class="card-contact">
      <div class="card-person">
        <p class="person-name">Daniel Reeve</p>
        <p class="person-title">Vicepresident</p>
      </div>
      <span class="card-divider"></span>
      <p class="card-address">4820 Larkmoor Pike, Suite 210<br>Nashville, TN&nbsp; 37211</p>
    </div>
  </section>

  <section class="sheet business-card card-single" aria-label="Business card">
    <span class="brand-mark" aria-hidden="true"></span>
    <h2 class="firm-name">The Farrowdale Penick Firm</h2>
    <div class="card-contact">
      <div class="card-person">
        <p class="person-name">Daniel Reeve</p>
        <p class="person-title">Vicepresident</p>
      </div>
      <span class="card-divider"></span>
      <p class="card-address">4820 Larkmoor Pike, Suite 210<br>Nashville, TN&nbsp; 37211</p>
    </div>
  </section>

  <section class="sheet envelope" aria-label="Envelope">
    <span class="brand-mark" aria-hidden="true"></span>
    <h2 class="firm-name">The Farrowdale Penick Firm</h2>
    <p class="address-line">4820 Larkmoor Pike, Suite 210 Nashville, TN&nbsp; 37211</p>
  </section>

</body>
</html>
```